Front book cover for a training course to help bakers get higher prices and sell more wedding cakes.

We need a front cover for a book that will be teaching bakers how to sell wedding cakes to get higher prices and book more orders. It is a business book. Do not make it look like we want brides to read it. Bakers will be judging the cover to see if it is worth their investment to read it. The title is already in the logo, so do not repeat it.

Target Market(s)

Bakers who sell wedding cakes

Industry/Entity Type

Bakery

Colors

Designer to choose colors to be used in the design.

Requirements
Must have
• Must use the logo. Must have author name: Lou Brand. Must have subtitle: Boost Your Prices. Book More Brides. Build Your Empire.
Nice to have
• You are free to be creative. The concept is not to be pretty. It is a business sales and marketing book

```html
<!DOCTYPE html>
<html lang="en">
<head>
<meta charset="utf-8">
<title>Tiered Profit Coach – Book Cover Spread</title>
<link rel="stylesheet" href="https://fonts.googleapis.com/css2?family=Montserrat:wght@500;600;700&family=Roboto:wght@700;900&display=swap">
<style>
  :root {
    --pink: #ec5178;
    --pink-soft: #f6b9c9;
    --pink-faint: #fbe3ea;
    --charcoal: #4a4a4c;
    --slate: #58585a;
    --text: #444446;
    --paper: #ffffff;
    --cover-bg: #f4f4f4;
    --page-bg: #ffffff;
  }
  * { box-sizing: border-box; margin: 0; padding: 0; }
  html, body {
    width: 1200px; height: 825px; overflow: hidden;
    background: var(--page-bg);
    font-family: "Montserrat", Arial, sans-serif;
  }
  .stage {
    position: relative;
    width: 1024px; height: 704px;
    transform: scale(1.171875);
    transform-origin: 0 0;
  }

  /* Back cover */
  .back-cover {
    position: absolute; left: 47px; top: 48px;
    width: 438px; height: 607px;
    background: var(--paper);
    box-shadow: 0 0 12px rgba(0,0,0,0.06);
    color: var(--text);
  }
  .author-label {
    position: absolute; left: 26px; top: 62px;
    font-size: 11.5px; font-weight: 500;
  }
  .section-title {
    position: absolute; left: 23px;
    font-size: 21px; font-weight: 700; letter-spacing: 0.1px;
  }
  .section-title span {
    display: inline-block; padding-bottom: 1px;
    border-bottom: 1.5px solid currentColor;
  }
  .section-title .accent { color: var(--pink); }
  .section-title .base { color: var(--charcoal); }
  .about-title { top: 89px; }
  .benefits-title { top: 326px; }
  .about-copy {
    position: absolute; left: 23px; top: 139px; width: 390px;
    font-size: 12.3px; line-height: 23px; font-weight: 500;
  }
  .about-copy p + p { margin-top: 8px; }
  .benefit-list {
    position: absolute; left: 22px; top: 370px;
    list-style: none; font-size: 12.3px; font-weight: 500;
  }
  .benefit-list li {
    display: flex; align-items: center; height: 25.5px;
  }
  .benefit-list svg { width: 10px; height: 10px; margin-right: 13px; }
  .back-brand {
    position: absolute; left: 20px; top: 548px;
    display: flex; align-items: center; gap: 8px;
    font-size: 21px; font-weight: 700; color: var(--charcoal);
  }
  .back-brand .mark {
    width: 14px; height: 14px; border-radius: 50%; background: var(--pink);
  }
  .contact-email {
    position: absolute; left: 248px; top: 570px;
    display: flex; align-items: center; gap: 7px;
    font-size: 12.3px; font-weight: 500;
  }

  /* Front cover */
  .front-cover {
    position: absolute; left: 485px; top: 48px;
    width: 490px; height: 607px;
    background: var(--cover-bg);
    overflow: hidden;
  }
  .front-shapes { position: absolute; inset: 0; }
  .front-brand {
    position: absolute; left: 50px; top: 68px; width: 150px;
    text-align: center;
    font-size: 22px; font-weight: 700; line-height: 24px; color: #fff;
  }
  .cover-line {
    position: absolute;
    font-family: "Roboto", Arial, sans-serif;
    font-weight: 900; color: var(--slate); letter-spacing: 0.3px;
  }
  .line-boost { right: 8px; top: 124px; font-size: 21.5px; }
  .line-empire { left: 55px; top: 497px; font-size: 21.5px; }
  .line-book {
    position: absolute; left: 54px; top: 360px;
    font-family: "Roboto", Arial, sans-serif; font-weight: 700;
    font-size: 46px; line-height: 36px; color: #fff; letter-spacing: -0.5px;
  }
  .line-book .o { color: var(--slate); }
  .byline {
    position: absolute; right: 10px; top: 577px;
    font-family: "Roboto", Arial, sans-serif; font-weight: 900;
    font-size: 16px; color: var(--charcoal); letter-spacing: 0.3px;
  }
</style>
</head>
<body>
<main class="stage">

  <section class="back-cover">
    <p class="author-label">Author Name: Lou Brand</p>

    <h2 class="section-title about-title"><span class="accent">About Tiered Profit</span> <span class="base">Coach</span></h2>
    <div class="about-copy">
      <p>Tiered Profit Coach is a specialized training program designed to help bakers and cake designers significantly increase their wedding cake sales &amp; profits.</p>
      <p>Developed by the National Cake Business Institute, it offers a comprehensive suite of tools, strategies, and insights aimed at transforming your approach to marketing and selling wedding cakes</p>
    </div>

    <h2 class="section-title benefits-title"><span class="accent">Potential</span> <span class="base">Benefits</span></h2>
    <ul class="benefit-list">
      <li><svg viewBox="0 0 10 10"><path d="M1 1 L9 5 L1 9 L3.5 5 Z" fill="var(--pink)"/></svg>Increased Sales</li>
      <li><svg viewBox="0 0 10 10"><path d="M1 1 L9 5 L1 9 L3.5 5 Z" fill="var(--pink)"/></svg>Higher Pricing Power</li>
      <li><svg viewBox="0 0 10 10"><path d="M1 1 L9 5 L1 9 L3.5 5 Z" fill="var(--pink)"/></svg>Competitive Advantage</li>
    </ul>

    <div class="back-brand"><span class="mark"></span>Tiered Profit Coach</div>

    <div class="contact-email">
      <svg width="20" height="16" viewBox="0 0 20 16" fill="none" stroke="var(--pink)" stroke-width="1.4">
        <rect x="1" y="2" width="18" height="13" rx="1.5"/>
        <path d="M1.5 3 L10 9.5 L18.5 3"/>
      </svg>
      hello@tieredprofit.com
    </div>
  </section>

  <section class="front-cover">
    <svg class="front-shapes" viewBox="0 0 490 607" width="490" height="607" aria-hidden="false">
      <defs>
        <linearGradient id="photoTone" x1="0" y1="0" x2="1" y2="1">
          <stop offset="0" stop-color="#e6e6e4"/>
          <stop offset="0.55" stop-color="#efe9e2"/>
          <stop offset="1" stop-color="#d9d6cf"/>
        </linearGradient>
      </defs>
      <polygon points="0,0 280,0 70,344 0,344" fill="var(--pink)"/>
      <polygon points="195,157 490,157 490,344 85,344" fill="url(#photoTone)" role="img" aria-label="Photo of a tall white tiered wedding cake with gold accents and pastel sugar flowers"/>
      <polygon points="0,350 278,350 203,484 0,484" fill="var(--pink)"/>
      <polygon points="287,350 395,350 305,484 212,484" fill="var(--slate)"/>
      <line x1="40" y1="0" x2="40" y2="607" stroke="var(--pink-soft)" stroke-width="1.5"/>
      <rect x="377" y="432" width="84" height="132" rx="6" fill="var(--pink-faint)" role="img" aria-label="Faint line drawing of a two-tier floral cake on a stand"/>
    </svg>

    <div class="front-brand">Tiered Profit Coach</div>

    <p class="cover-line line-boost">BOOST YOUR PRICES.</p>
    <h1 class="line-book">BOOK<br>M<span class="o">O</span>RE<br>BRIDES</h1>
    <p class="cover-line line-empire">BUILD YOUR EMPIRE.</p>
    <p class="byline">BY LOU BRAND</p>
  </section>

</main>
</body>
</html>
```